Dorrington Thermal Heating and Air Conditioning web page

This is a repair, installation and maintenance residential company. I don't do commercial. I need a web design that shows a company with 24/7 fast service that is easy for customers to contact me from. I am a Brackley /Tovex HVAC dealer and their logos can be on there also. I also sell IAQ products like Zenta- Orbit and I offer duct cleanings as well.

Industry/Entity Type

Hvac

Coding

Coded - Design and coding required

Number of Pages Required

2 page

```html
<!DOCTYPE html>
<html lang="en">
<head>
<meta charset="utf-8">
<title>Dorrington Thermal Heating and Air Conditioning</title>
<link href="https://fonts.googleapis.com/css2?family=Rajdhani:wght@300;500;600;700&family=Heebo:wght@400;500;700&display=swap" rel="stylesheet">
<style>
:root{
  --red:#e8141c;
  --blue:#0a9be6;
  --black:#0a0a0a;
  --dark:#1c1c1d;
  --white:#ffffff;
  --text:#222;
  --field:#ececec;
  --head:'Rajdhani',sans-serif;
  --body:'Heebo',sans-serif;
}
*{box-sizing:border-box;margin:0;padding:0}
html,body{width:1200px;height:3866px;overflow:hidden}
body{position:relative;background:var(--white);font-family:var(--body);color:var(--text)}
.abs{position:absolute}
.backdrop{position:absolute;left:0;top:0;width:1200px;height:3866px}
.photo{position:absolute}
.hero-photo{left:0;top:0;width:1200px;height:640px;background:linear-gradient(100deg,#2a3340 0%,#1a1d22 45%,#2d2f33 100%);clip-path:polygon(0 0,1200px 0,1200px 322px,0 630px)}
.worker-photo{left:990px;top:360px;width:210px;height:690px;background:linear-gradient(180deg,#1f4fa8 0%,#153c86 60%,#0e2a60 100%);border-radius:100px 0 0 0}
.skyline{left:0;top:1590px;width:1200px;height:458px;background:linear-gradient(180deg,#1e1f21 0%,#2f3134 55%,#242527 100%)}
.gauge-photo{left:0;top:2362px;width:195px;height:743px;background:linear-gradient(160deg,#b07a68 0%,#2a4f86 45%,#1e67c0 70%,#b31d22 100%);border-radius:0 60px 60px 0}

.logo{font-family:var(--head);font-weight:700;color:var(--white);font-size:27px;line-height:1;letter-spacing:1px;text-transform:uppercase}
.logo .mark{display:inline-block;width:12px;height:12px;background:var(--blue);margin-left:4px}
.site-logo{left:248px;top:22px;width:190px}
.top-info{top:30px;display:flex;align-items:center;gap:10px;color:var(--white)}
.top-info svg{width:24px;height:24px}
.top-info small{display:block;font-size:10px;color:var(--blue)}
.top-info strong{display:block;font-family:var(--head);font-weight:700;font-size:17px;letter-spacing:.3px}
.nav{left:248px;top:101px;font-family:var(--head);font-weight:500;font-size:15px;color:var(--white)}
.nav a{color:inherit;text-decoration:none;position:absolute;white-space:nowrap}
.nav .active{color:var(--blue)}
.search{left:934px;top:102px;width:16px;height:16px}

.hero-title{left:0;width:1200px;text-align:center;font-family:var(--head)}
.hero-title .l1{position:absolute;top:200px;width:100%;font-weight:300;font-size:44px;color:#e9e9e9}
.hero-title .l2{position:absolute;top:240px;width:100%;font-weight:500;font-size:62px;color:var(--blue);letter-spacing:1px}
.hero-title .l3{position:absolute;top:303px;width:100%;font-weight:700;font-size:33px;color:var(--red);letter-spacing:.5px}

.offer{top:480px;width:218px;height:218px;background:#888}
.offer .pic{height:186px}
.offer .label{height:32px;background:var(--red);color:var(--white);font-family:var(--head);font-weight:700;font-size:14px;padding:7px 11px}

.section-title{left:0;width:1200px;text-align:center;font-family:var(--head);font-weight:700;font-size:17px;letter-spacing:.3px;color:var(--black)}
.intro{left:360px;width:480px;text-align:center;font-size:11.5px;line-height:18px;color:#333}
.btn{display:flex;align-items:center;justify-content:center;background:var(--red);color:var(--white);font-family:var(--head);font-weight:700;font-size:12px}
.btn.blue{background:var(--blue)}

.service{width:341px;height:195px;background:var(--white);box-shadow:0 2px 12px rgba(0,0,0,.12);padding:40px 26px 0 96px}
.service.dark{background:var(--black);color:var(--white)}
.service svg{position:absolute;left:24px;top:36px;width:58px;height:54px}
.service h3{font-family:var(--head);font-weight:700;font-size:14px;margin-bottom:12px}
.service p{font-size:10.5px;line-height:17.5px}

.why-kicker{left:0;width:1200px;text-align:center;font-family:var(--head);font-weight:700;font-size:16px;color:var(--blue)}
.why-title{left:0;width:1200px;text-align:center;font-family:var(--head);font-weight:500;font-size:23px;color:var(--white)}
.feature{width:200px;color:var(--white)}
.feature h4{font-family:var(--head);font-weight:700;font-size:14px;color:var(--blue);margin-bottom:6px}
.feature p{font-size:10.5px;line-height:13px}
.feature.left{text-align:right}
.truck{left:368px;top:1790px;width:450px;height:140px;background:linear-gradient(180deg,#3a3b3e,#111);border-radius:40px 60px 20px 20px}

.product{width:294px;height:208px;background:linear-gradient(135deg,#8c97a3,#5b6570);color:var(--white);text-align:center}
.product h3{margin-top:84px;font-family:var(--head);font-weight:700;font-size:17px;letter-spacing:.3px}
.product p{font-size:10px;margin-top:4px}

.price-card{top:2830px;width:205px;height:338px;background:var(--white);box-shadow:0 3px 14px rgba(0,0,0,.13);text-align:center;padding:28px 20px 0}
.price-card.dark{background:var(--black);color:var(--white)}
.price-card h3{font-family:var(--head);font-weight:700;font-size:14px;line-height:15px;height:36px}
.price-card .price{font-family:var(--head);font-weight:300;font-size:44px;color:var(--red);line-height:1;margin:8px 0 18px}
.price-card .price sup{font-size:20px;vertical-align:top;margin-right:3px;position:relative;top:2px}
.price-card p{font-size:10px;line-height:17.5px}
.price-card .btn{position:absolute;left:58px;bottom:24px;width:88px;height:32px}

.form-box{left:249px;top:3322px;width:454px;height:333px;background:var(--white)}
.form-box h3{position:absolute;top:25px;width:100%;text-align:center;font-family:var(--head);font-weight:700;font-size:16px}
.field{background:var(--field);font-size:10px;color:#777;padding:7px 12px}
.experts h3{font-family:var(--head);font-weight:700;font-size:16px;color:var(--white)}
.expert{left:733px;color:var(--white);display:flex;gap:14px}
.expert svg{width:22px;height:22px;margin-top:4px;flex:none}
.expert small{display:block;font-size:10px;color:var(--blue)}
.expert strong{display:block;font-family:var(--head);font-weight:700;font-size:17px;line-height:18.5px}

.footer-rule{left:249px;top:3702px;width:702px;height:1px;background:#555}
.footer-logo{left:0;top:3740px;width:1200px;text-align:center}
.copyright{left:0;top:3812px;width:1200px;text-align:center;font-size:9.5px;color:#ddd}
.copyright .dealer{color:var(--blue)}
</style>
</head>
<body>

<svg class="backdrop" viewBox="0 0 1200 3866" aria-hidden="true">
  <rect x="0" y="0" width="1200" height="640" fill="#141416"/>
  <polygon points="0,630 1200,322 1200,640 0,640" fill="#fff"/>
  <polygon points="0,1290 1200,1025 1200,2175 0,2360" fill="#1c1c1d"/>
  <polygon points="0,3520 1200,3200 1200,3866 0,3866" fill="#1c1c1d"/>
</svg>

<div class="photo hero-photo" role="img" aria-label="Technician checking an outdoor air conditioning unit with pressure gauges"></div>
<div class="photo worker-photo" role="img" aria-label="Smiling HVAC technician in blue overalls with a tool belt, arms crossed"></div>
<div class="photo skyline" role="img" aria-label="Dark city skyline at dusk"></div>
<div class="photo gauge-photo" role="img" aria-label="Hand holding a blue refrigerant manifold gauge with red and blue hoses"></div>

<div class="abs site-logo logo">Dorrington<span class="mark"></span><br>Thermal</div>

<div class="abs top-info" style="left:488px">
  <svg viewBox="0 0 24 24" fill="none" stroke="#0a9be6" stroke-width="1.6"><path d="M5 3h4l2 5-2.5 1.5a11 11 0 0 0 6 6L16 13l5 2v4a2 2 0 0 1-2 2A16 16 0 0 1 3 5a2 2 0 0 1 2-2z"/></svg>
  <div><small>24/7 Call Us Today</small><strong>000-000-0000</strong></div>
</div>
<div class="abs top-info" style="left:656px">
  <svg viewBox="0 0 24 24" fill="none" stroke="#0a9be6" stroke-width="1.6"><circle cx="12" cy="12" r="10"/><path d="M12 6v6l4 2"/></svg>
  <div><small>Work Time</small><strong>8:00 - 18:00</strong></div>
</div>
<div class="abs top-info" style="left:813px">
  <svg viewBox="0 0 24 24" fill="none" stroke="#0a9be6" stroke-width="1.6"><path d="M12 22s7-7 7-12a7 7 0 0 0-14 0c0 5 7 12 7 12z"/><circle cx="12" cy="10" r="2.5"/></svg>
  <div><small>ABC Street City</small><strong>Street City 123</strong></div>
</div>

<nav class="abs nav">
  <a class="active" style="left:0">Home</a>
  <a style="left:82px">About</a>
  <a style="left:165px">Services</a>
  <a style="left:259px">Products</a>
  <a style="left:358px">Pricing</a>
  <a style="left:445px">Contacts</a>
</nav>
<svg class="abs search" viewBox="0 0 16 16" fill="none" stroke="#e8141c" stroke-width="1.8"><circle cx="6.5" cy="6.5" r="5"/><path d="M10.5 10.5 15 15"/></svg>

<div class="abs hero-title">
  <div class="l1">REPAIR</div>
  <div class="l2">INSTALLATION</div>
  <div class="l3">HEATING AND AIR CONDITIONING</div>
</div>

<div class="abs offer" style="left:249px"><div class="pic" role="img" aria-label="Technician servicing a wall-mounted air conditioner" style="background:linear-gradient(180deg,#d9dde2,#2f4f8f)"></div><div class="label">Repair</div></div>
<div class="abs offer" style="left:492px"><div class="pic" role="img" aria-label="Technician kneeling to install equipment" style="background:linear-gradient(180deg,#e6e8ea,#30508a)"></div><div class="label">Installation</div></div>
<div class="abs offer" style="left:734px"><div class="pic" role="img" aria-label="Technician with a toolbox in a residential kitchen" style="background:linear-gradient(180deg,#8d8f92,#d8d8d8)"></div><div class="label">Maintenance Residential</div></div>

<h2 class="abs section-title" style="top:781px">WELCOME TO DORRINGTON THERMAL</h2>
<p class="abs intro" style="top:816px">We are a residential heating and air conditioning company offering fast 24/7 repair, installation and maintenance. As an authorized Brackley and Tovex dealer, we keep your home comfortable all year round.</p>
<div class="abs btn" style="left:558px;top:885px;width:84px;height:29px">About</div>

<h2 class="abs section-title" style="top:999px">SERVICES</h2>

<div class="abs service dark" style="left:249px;top:1070px">
  <svg viewBox="0 0 58 54" fill="none" stroke="#e8141c" stroke-width="2"><rect x="3" y="6" width="22" height="30" rx="3"/><path d="M8 14h12M8 20h12M8 26h12M14 36v10h14"/><rect x="30" y="8" width="10" height="18" rx="2"/><path d="M44 10h6M44 16h6M44 22h6M35 26v8"/></svg>
  <h3>Heater Repair</h3>
  <p>Fast 24/7 repair for furnaces and heat pumps. Our technicians arrive quickly, find the fault and get your home warm again the same day.</p>
</div>
<div class="abs service" style="left:610px;top:1070px">
  <svg viewBox="0 0 58 54" fill="none" stroke="#e8141c" stroke-width="2"><path d="M6 14h28a6 6 0 1 0-6-6M6 24h40a6 6 0 1 1-6 6M6 34h22a5 5 0 1 1-5 5M40 14h8M34 40h4M44 40h4"/></svg>
  <h3>Indoor Air Quality</h3>
  <p>Breathe cleaner air at home with IAQ products such as Zenta- Orbit air purifiers, filters and humidity control fitted by our team.</p>
</div>
<div class="abs service" style="left:249px;top:1280px">
  <svg viewBox="0 0 58 54" fill="none" stroke="#e8141c" stroke-width="2"><path d="M4 26h50v10H4zM10 26V16h10v10M34 26V12h12v14M8 16h14M32 12h16"/><path d="M40 40v10M46 40v10M52 40v10"/></svg>
  <h3>Duct cleaning &amp; Installation</h3>
  <p>We clean dust and debris from your ductwork and install new ducts, so air flows freely and your system runs efficiently.</p>
</div>
<div class="abs service" style="left:610px;top:1280px">
  <svg viewBox="0 0 58 54" fill="none" stroke="#e8141c" stroke-width="2"><rect x="12" y="4" width="26" height="40" rx="3"/><circle cx="25" cy="20" r="6"/><path d="M25 10v3M25 27v3M15 20h3M32 20h3M6 30h12M32 30h14M18 36h14M20 50h10"/></svg>
  <h3>Residential AC Maintenance</h3>
  <p>Seasonal tune-ups for home air conditioners keep your system reliable, lower energy bills and prevent costly breakdowns.</p>
</div>
<div class="abs btn" style="left:552px;top:1512px;width:96px;height:30px">Service More</div>

<div class="abs why-kicker" style="top:1608px">WHY WORK WITH US</div>
<div class="abs why-title" style="top:1634px">Heating and Air Conditioning</div>

<svg class="abs" style="left:490px;top:1742px" width="220" height="220" viewBox="0 0 220 220" fill="none" stroke="#0a9be6" stroke-width="9" stroke-linecap="round"><path d="M30 92A82 82 0 0 1 190 92"/><path d="M190 150A82 82 0 0 1 30 150"/></svg>
<div class="abs photo truck" role="img" aria-label="Black company pickup truck"></div>

<div class="abs feature left" style="left:238px;top:1712px"><h4>• Cost Effective</h4><p>We make prioritized,<br>cost-effective recommendations<br>to better seal your home.</p></div>
<div class="abs feature" style="left:752px;top:1712px"><h4>• Energy Efficient</h4><p>We help you determine which<br>energy efficient supplies will best<br>meet your needs.</p></div>
<div class="abs feature left" style="left:238px;top:1950px"><h4>• Healthy</h4><p>Let our professionals create a<br>healthy home environment for<br>those you care about.</p></div>
<div class="abs feature" style="left:752px;top:1950px"><h4>• Quick</h4><p>In no time, we can locate the<br>source of your HVAC problem and<br>perform repairs.</p></div>

<h2 class="abs section-title" style="top:2107px;color:var(--red)">PRODUCTS</h2>

<div class="abs product" style="left:152px;top:2200px" role="img" aria-label="Hands opening an indoor AC unit"><h3>AC MAINTENANCE</h3><p>Lorem Ipsum has been the industry.</p></div>
<div class="abs product" style="left:453px;top:2200px" role="img" aria-label="Technician drilling during AC installation"><h3>AC INSTALLATION</h3><p>Lorem Ipsum has been the industry.</p></div>
<div class="abs product" style="left:755px;top:2200px" role="img" aria-label="Hand tightening a fitting on an AC unit"><h3>AC REPAIR</h3><p>Lorem Ipsum has been the industry.</p></div>
<div class="abs product" style="left:152px;top:2412px" role="img" aria-label="Manifold gauges next to a heating unit"><h3>HEATING CHECKUP</h3><p>Lorem Ipsum has been the industry.</p></div>
<div class="abs product" style="left:453px;top:2412px;background:linear-gradient(135deg,#c9ccd0,#9aa0a6)" role="img" aria-label="Ceiling-mounted heating unit"><h3>HEATING INSTALATION</h3><p>Lorem Ipsum has been the industry.</p></div>
<div class="abs product" style="left:755px;top:2412px;background:linear-gradient(135deg,#b9a792,#7d7268)" role="img" aria-label="Open AC unit with exposed circuit board"><h3>AC MAINTENANCE</h3><p>Lorem Ipsum has been the industry.</p></div>

<div class="abs btn" style="left:537px;top:2655px;width:128px;height:32px">ALL More Products</div>

<h2 class="abs section-title" style="top:2770px">OUR PRICING</h2>

<div class="abs price-card dark" style="left:260px">
  <h3>Heating Repair</h3>
  <div class="price"><sup>$</sup>79.89</div>
  <p>We understand that any kind of a problem with the heating system in the winter is ought to be fixed immediately! Overall we provide heating services such as repairs, maintenance, replacements and installations.</p>
  <div class="btn">Buy Now</div>
</div>
<div class="abs price-card" style="left:498px">
  <h3>Air Conditioning<br>Maintenance</h3>
  <div class="price"><sup>$</sup>89.89</div>
  <p>Unless you do a proper yearly maintenance for all of your AC units, indoors and outdoors – bad consequences are inevitable. Overall we provide air conditioning services such as repairs and installations.</p>
  <div class="btn">Buy Now</div>
</div>
<div class="abs price-card" style="left:735px">
  <h3>Heating Maintenance</h3>
  <div class="price"><sup>$</sup>99.89</div>
  <p>For sure we all know how important hardware home appliance maintenance is. It's just that it takes booking a pro in order to do it. Overall we provide heating services such as repairs and installations.</p>
  <div class="btn">Buy Now</div>
</div>

<h2 class="abs section-title" style="top:3253px">CONTACT</h2>

<div class="abs form-box">
  <h3>SCHEDULE AN APPOINTMENT</h3>
  <div class="abs field" style="left:30px;top:62px;width:191px;height:30px">Name</div>
  <div class="abs field" style="left:233px;top:62px;width:190px;height:30px">Email</div>
  <div class="abs field" style="left:30px;top:104px;width:191px;height:31px">Phone</div>
  <div class="abs field" style="left:233px;top:104px;width:190px;height:31px">Address</div>
  <div class="abs field" style="left:30px;top:146px;width:393px;height:117px">Comment</div>
  <div class="abs btn blue" style="left:183px;top:284px;width:86px;height:30px">Buy Now</div>
</div>

<div class="abs experts" style="left:733px;top:3342px"><h3>CONTACT EXPERTS</h3></div>
<div class="abs expert" style="top:3388px">
  <svg viewBox="0 0 24 24" fill="none" stroke="#0a9be6" stroke-width="1.6"><path d="M5 3h4l2 5-2.5 1.5a11 11 0 0 0 6 6L16 13l5 2v4a2 2 0 0 1-2 2A16 16 0 0 1 3 5a2 2 0 0 1 2-2z"/></svg>
  <div><small>24/7 Call Us Today</small><strong>000-000-0000</strong></div>
</div>
<div class="abs expert" style="top:3445px">
  <svg viewBox="0 0 24 24" fill="none" stroke="#0a9be6" stroke-width="1.6"><rect x="3" y="8" width="5" height="14"/><rect x="8" y="4" width="13" height="18"/><path d="M11 8h7M11 12h2M15 12h2M11 16h2M15 16h2"/></svg>
  <div><small>Fax</small><strong>000-000-0000</strong></div>
</div>
<div class="abs expert" style="top:3500px">
  <svg viewBox="0 0 24 24" fill="none" stroke="#0a9be6" stroke-width="1.6"><path d="M12 22s7-7 7-12a7 7 0 0 0-14 0c0 5 7 12 7 12z"/><circle cx="12" cy="10" r="2.5"/></svg>
  <div><small>ABC Street City</small><strong>Street City 123</strong></div>
</div>
<div class="abs expert" style="top:3556px">
  <svg viewBox="0 0 24 24" fill="none" stroke="#0a9be6" stroke-width="1.6"><circle cx="12" cy="12" r="10"/><path d="M12 6v6l4 2"/></svg>
  <div><small>Work Time</small><strong>Monday-Friday<br>8AM - 18PM<br>Saturday-Sunday<br>10AM - 3PM</strong></div>
</div>

<div class="abs footer-rule"></div>
<div class="abs footer-logo logo">Dorrington<span class="mark"></span><br>Thermal</div>
<div class="abs copyright">© 2020 Dorrington Thermal. All Rights Reserved. &nbsp; | &nbsp; <span class="dealer">Authorized Brackley / Tovex Dealer</span></div>

</body>
</html>
```